Lumen Cove Skincare - Package Design

New Beauty label needing product packaging design. Looking for elegant and stylish design to represent our premium brand.

This project is for 1 label and 1 box design. The winning designer will be assigned another project for the next product in the range. (to be paid as a new project)

This product is for "Dead Sea Mud Mask". Please see the label format and jar attached. Please note there are 2 different jars we are considering (will have a mud inside). Please feel free to choose whichever one suits your design best.

The labels and boxes are to retain the product information, such as size, ingredients etc, but is to be updated to our brand. You can move or display the other information as you wish.

the size of the dead sea mud mask color box is 72*72*85mm (length*width*height)
the size of dead sea mud mask label is 218*58mm (width*height)

Target Market(s)

Women 15 to 65

Requirements
Must have
• Must be elegant and represent our brand which is a premium beauty product.
Should not have
• Dark blue. Dark purple etc. Colours should compliment the logo

```html
<!DOCTYPE html>
<html lang="en">
<head>
<meta charset="utf-8">
<title>Lumen Cove Skincare – Dead Sea Mud Mask Packaging</title>
<link href="https://fonts.googleapis.com/css2?family=Playfair+Display:wght@500&family=Arimo:ital@1&display=swap" rel="stylesheet">
<style>
  :root {
    --backdrop: #ecebe7;
    --box-black: #1c1b1a;
    --label-black: #201f1d;
    --label-pattern: #2b2a27;
    --gold: #b8963f;
    --silver: #c9c7c2;
  }
  * { margin: 0; padding: 0; box-sizing: border-box; }
  html, body { width: 1200px; height: 992px; overflow: hidden; }
  body {
    background: var(--backdrop);
    position: relative;
    font-family: "Arimo", Arial, sans-serif;
  }
  .panel { position: absolute; display: flex; flex-direction: column; align-items: center; }

  .box-front {
    left: 390px; top: 48px; width: 420px; height: 496px;
    background: var(--box-black);
    padding-top: 78px;
  }
  .label {
    left: 80px; top: 640px; width: 1040px; height: 276px;
    justify-content: center;
  }
  .label-texture {
    position: absolute; inset: 0;
    background: radial-gradient(ellipse at center, var(--label-pattern), var(--label-black) 75%);
  }
  .label-content { position: relative; display: flex; flex-direction: column; align-items: center; }

  .brand-name {
    font-family: "Playfair Display", Georgia, serif;
    font-weight: 500;
    color: var(--gold);
    letter-spacing: 0.5px;
  }
  .box-front .brand-name { font-size: 34px; }
  .label .brand-name { font-size: 24px; }

  .product-title {
    font-family: "Playfair Display", Georgia, serif;
    font-weight: 500;
    color: var(--gold);
    text-transform: uppercase;
    transform: scaleX(0.82);
    white-space: nowrap;
  }
  .box-front .product-title { font-size: 46px; margin-top: 70px; }
  .label .product-title { font-size: 38px; margin-top: 26px; }

  .claims {
    font-style: italic;
    color: var(--silver);
    text-align: center;
    line-height: 1.25;
  }
  .box-front .claims { font-size: 19px; margin-top: 18px; }
  .label .claims { font-size: 15px; margin-top: 10px; }

  .ingredients-note {
    font-style: italic;
    color: var(--silver);
    text-align: center;
    font-size: 15px;
    line-height: 1.35;
    margin-top: 92px;
  }
  .net-weight {
    font-style: italic;
    color: var(--silver);
    font-size: 15px;
    margin-top: 22px;
  }
</style>
</head>
<body>

  <section class="panel box-front" aria-label="Box front panel">
    <p class="brand-name">Lumen Cove Skincare</p>
    <h1 class="product-title">Dead Sea Mud Mask</h1>
    <p class="claims">Acne. Pores, Blackheads,<br>Whiteheads and Breakouts</p>
    <p class="ingredients-note">Simply formulated using high quality 100 % natural<br>ingredients mineral dead sea mud</p>
  </section>

  <section class="panel label" aria-label="Jar label">
    <div class="label-texture" role="img" aria-label="Subtle dark leaf-scatter pattern across the label"></div>
    <div class="label-content">
      <p class="brand-name">Lumen Cove Skincare</p>
      <h2 class="product-title">Dead Sea Mud Mask</h2>
      <p class="claims">Acne. Pores, Blackheads,<br>Whiteheads and Breakouts</p>
      <p class="net-weight">250g - 8.8 fl. Oz</p>
    </div>
  </section>

</body>
</html>
```